ALL TEXT GRAPHICS RK May 2025 for Instagram

We are looking for a series of social media graphics for Instagram (new size: 4:5 (1080 x 1350 pixels) ratio that are ALL TEXT. We want the following quotes below on each graphic; one quote per graphic. AND, In very small letters at the bottom of each graphic, add @RKBexleyOnline
The look and feel of these graphics should be complimentary to the color palette attached below; but keep them simple. But the design is up to you; at the end of this document, I provided various samples of all text graphics that I like as examples.
women looking to lose weight

```html
<!DOCTYPE html>
<html lang="en">
<head>
<meta charset="utf-8">
<title>RK Instagram Text Graphics</title>
<link href="https://fonts.googleapis.com/css2?family=Cormorant+Garamond:wght@700&family=Quicksand:wght@600;700&display=swap" rel="stylesheet">
<style>
  :root {
    --page-bg: #e6e2e3;
    --card-bg: #ffffff;
    --pink-deep: #cf0f6c;
    --pink-bright: #f0147c;
    --pink-glow: #ff6fb2;
    --ink: #0d0d0d;
    --frame: #ffffff;
  }
  * { margin: 0; padding: 0; box-sizing: border-box; }
  html, body {
    width: 1200px;
    height: 4164px;
    overflow: hidden;
    background: var(--page-bg);
  }
  .post {
    position: absolute;
    left: 108px;
    width: 1001px;
    height: 1251px;
    background: var(--card-bg);
    overflow: hidden;
    box-shadow: 0 0 40px rgba(120, 90, 100, 0.12);
  }
  .post--one { top: 86px; }
  .post--two { top: 1441px; }
  .post--three { top: 2796px; }

  .post--glow-tl-br {
    background:
      radial-gradient(ellipse 520px 360px at 0% 0%, var(--pink-glow) 0%, rgba(255,111,178,0.45) 30%, rgba(255,255,255,0) 75%),
      radial-gradient(ellipse 520px 480px at 100% 100%, var(--pink-glow) 0%, rgba(255,111,178,0.45) 30%, rgba(255,255,255,0) 75%),
      var(--card-bg);
  }
  .post--glow-tr-bl {
    background:
      radial-gradient(ellipse 380px 620px at 100% 0%, var(--pink-glow) 0%, rgba(255,111,178,0.45) 30%, rgba(255,255,255,0) 75%),
      radial-gradient(ellipse 560px 260px at 0% 100%, var(--pink-glow) 0%, rgba(255,111,178,0.45) 30%, rgba(255,255,255,0) 75%),
      var(--card-bg);
  }

  .corner {
    position: absolute;
    width: 145px;
    height: 145px;
    border-color: var(--frame);
    border-style: solid;
    border-width: 0;
  }
  .corner--tl { top: 31px; left: 53px; border-top-width: 3px; border-left-width: 3px; }
  .corner--tr { top: 46px; right: 51px; border-top-width: 3px; border-right-width: 3px; }
  .corner--br { bottom: 36px; right: 31px; border-bottom-width: 3px; border-right-width: 3px; }

  .kicker, .headline, .cta, .handle {
    position: absolute;
    left: 49px;
    white-space: nowrap;
  }
  .kicker {
    font-family: "Quicksand", sans-serif;
    font-weight: 700;
    font-size: 62px;
    line-height: 93px;
    color: var(--pink-deep);
  }
  .headline {
    font-family: "Cormorant Garamond", serif;
    font-weight: 700;
    font-size: 86px;
    line-height: 102px;
    text-transform: uppercase;
    color: var(--ink);
  }
  .cta {
    font-family: "Quicksand", sans-serif;
    font-weight: 700;
    font-size: 50px;
    line-height: 92px;
    color: var(--pink-bright);
  }
  .handle {
    font-family: "Quicksand", sans-serif;
    font-weight: 700;
    font-size: 27px;
    line-height: 34px;
    color: var(--ink);
  }
  .spark {
    position: absolute;
    width: 70px;
    height: 80px;
  }
  .spark line {
    stroke-width: 6;
    stroke-linecap: round;
  }
</style>
</head>
<body>

<section class="post post--one post--glow-tl-br">
  <span class="corner corner--tl"></span>
  <span class="corner corner--br"></span>
  <p class="kicker" style="top: 270px;">Tired. Moody. Stubborn<br>Belly Fat.</p>
  <svg class="spark" style="left: 852px; top: 262px;" viewBox="0 0 70 80" aria-hidden="true">
    <line x1="10" y1="6" x2="10" y2="20" stroke="var(--pink-deep)"/>
    <line x1="44" y1="14" x2="36" y2="24" stroke="var(--pink-deep)"/>
    <line x1="40" y1="68" x2="58" y2="68" stroke="var(--pink-deep)"/>
  </svg>
  <h2 class="headline" style="top: 541px;">Your hormones<br>are screaming<br>for help!</h2>
  <p class="cta" style="top: 885px;">Let's fix that.</p>
  <p class="handle" style="top: 1170px;">@RKBexleyOnline</p>
</section>

<section class="post post--two post--glow-tr-bl">
  <span class="corner corner--tr"></span>
  <p class="kicker" style="top: 164px;">That stubborn weight?</p>
  <h2 class="headline" style="top: 293px;">It's not your<br>fault.<br>Your hormones<br>are to blame and<br>you're<br>not alone;</h2>
  <p class="cta" style="top: 941px;">But there is a fix.</p>
  <svg class="spark" style="left: 466px; top: 928px;" viewBox="0 0 70 80" aria-hidden="true">
    <line x1="10" y1="6" x2="10" y2="20" stroke="var(--pink-bright)"/>
    <line x1="44" y1="14" x2="36" y2="24" stroke="var(--pink-bright)"/>
    <line x1="40" y1="68" x2="58" y2="68" stroke="var(--pink-bright)"/>
  </svg>
  <p class="handle" style="top: 1171px;">@RKBexleyOnline</p>
</section>

<section class="post post--three post--glow-tl-br">
  <span class="corner corner--tl"></span>
  <span class="corner corner--br"></span>
  <p class="kicker" style="top: 245px;">Your belly isn't fat...</p>
  <h2 class="headline" style="top: 371px;">It's<br>hormonal.<br>And here's<br>how to fix it.</h2>
  <p class="cta" style="top: 802px;">Comment<br>HORMONES if nothing is working.</p>
  <p class="handle" style="top: 1171px;">@RKBexleyOnline</p>
</section>

</body>
</html>
```